Redesign of current website

Redesign - tmrdbllc.com

Coding

Coded - Design and coding required

Number of Pages Required

4 page

Colors

Designer to choose colors to be used in the design.

```html
<!DOCTYPE html>
<html lang="en">
<head>
<meta charset="utf-8">
<title>TMRDB, LLC — Surveillance Camera Installations &amp; Training</title>
<link href="https://fonts.googleapis.com/css2?family=Roboto:wght@400;500;700&display=swap" rel="stylesheet">
<style>
:root{
  --green:#22a514;
  --green-dark:#178a0b;
  --green-light:#3cc22a;
  --ink:#1d1d1d;
  --text:#444;
  --muted:#666;
  --grey-bg:#e9e9e9;
  --grey-band:#a9a9a9;
  --footer:#2b2b2b;
  --footer-bar:#222;
  --white:#fff;
}
*{margin:0;padding:0;box-sizing:border-box}
html,body{width:1200px;height:3382px;overflow:hidden}
body{position:relative;font-family:'Roboto',Arial,sans-serif;color:var(--text);background:var(--white)}
.abs{position:absolute}

/* hero */
.hero{left:0;top:0;width:1200px;height:735px;
  clip-path:polygon(0 0,100% 0,100% 643px,50% 735px,0 643px);
  background:linear-gradient(180deg,#2a52c9 0%,#3a62c8 35%,#6a6f8e 58%,#8b5f3a 75%,#4a3322 100%)}
.topbar{color:var(--white);font-size:16px}
.mail-icon{display:inline-block;vertical-align:middle;margin-right:6px}
.nav a{position:absolute;top:86px;color:var(--white);text-decoration:none;font-size:14px;font-weight:500;white-space:nowrap}
.nav a.active::after{content:"";position:absolute;left:0;right:0;top:24px;height:2px;background:var(--white)}
.brand{left:480px;top:22px;width:240px;text-align:center;color:var(--white);font-weight:700;font-size:34px;letter-spacing:2px}
.brand small{display:block;font-size:13px;font-weight:700;letter-spacing:1px;margin-top:6px}
.hero-title{left:167px;top:276px;color:var(--white)}
.hero-title h1{font-size:41px;font-weight:700;line-height:48px}
.hero-title h2{font-size:36px;font-weight:400;line-height:44px}
.hero-title p{font-size:19px;line-height:27px;margin-top:22px}
.btn-solid{display:block;background:var(--green);color:var(--white);font-weight:700;font-size:16px;border-radius:26px;text-align:center;text-decoration:none}
.dots{left:558px;top:680px;display:flex;gap:8px}
.dots span{width:14px;height:14px;border-radius:50%;background:var(--white)}
.dots span.on{background:transparent;border:2px solid var(--white)}

/* intro */
.intro{left:0;width:1200px;text-align:center;color:var(--ink)}
.intro h2{font-size:38px;font-weight:700}
.intro h3{font-size:23px;font-weight:500;margin-top:4px}
.intro p{width:830px;margin:24px auto 0;font-size:16.5px;line-height:27px;color:var(--text)}

.card{top:1046px;width:303px;height:242px;background:var(--white);border:2px solid #ddd;text-align:center}
.card .ico{position:absolute;left:107px;top:-38px;width:90px;height:90px;border-radius:50%;background:var(--green);display:flex;align-items:center;justify-content:center}
.card .ico.dark{background:#444}
.card h4{margin-top:70px;font-size:18px;font-weight:700;color:var(--ink)}
.card p{margin:10px auto 0;width:265px;font-size:12px;line-height:18px;color:var(--text)}
.btn-line{display:block;border:2px solid var(--green);color:var(--green);font-weight:700;font-size:13px;border-radius:22px;text-align:center;text-decoration:none;background:transparent}
.card .btn-line{position:absolute;left:78px;top:168px;width:144px;height:42px;line-height:38px}

/* services */
.grey-bg{left:0;top:1300px;width:1200px;height:1400px;background:var(--grey-bg)}
.services-band{left:0;top:1300px;width:1200px;height:700px}
.services-head{left:0;top:1466px;width:1200px;text-align:center;color:var(--white)}
.services-head h2{font-size:30px;font-weight:700}
.services-head p{width:880px;margin:14px auto 0;font-size:17px;line-height:27px}
.tile{top:1628px;width:307px;height:353px;overflow:hidden}
.tile .label{position:absolute;left:0;right:0;bottom:24px;text-align:center;color:var(--white);font-size:22px;font-weight:700}
.tile.training{background:linear-gradient(160deg,#3b3b3b,#1e1e1e)}
.tile.training .inner{text-align:center;color:var(--white);padding-top:70px}
.tile.training h3{font-size:22px;font-weight:700}
.tile.training p{width:230px;margin:12px auto 0;font-size:13px;line-height:23px}
.tile.training .btn-line{width:158px;height:44px;line-height:40px;margin:32px auto 0}

.feature{left:119px;top:2066px;width:971px;height:413px;background:var(--white)}
.feature .photo{position:absolute;left:0;top:0;width:481px;height:413px;background:linear-gradient(135deg,#3c6fb0 0%,#8cb2d6 45%,#5b7f5a 100%)}
.feature .copy{position:absolute;left:544px;top:58px;width:380px}
.feature h3{font-size:27px;font-weight:700;line-height:31px;color:var(--ink)}
.feature p{font-size:14px;line-height:25px;color:var(--text);margin-top:14px}
.feature .btn-line{width:157px;height:44px;line-height:40px;margin-top:28px}

/* partners */
.partners-title{left:0;top:2700px;width:1182px;text-align:center;font-size:30px;font-weight:700;color:var(--ink)}
.partner{top:2776px;width:205px;height:107px;border:2px solid #e6e6e6;background:var(--white);display:flex;align-items:center;justify-content:center;gap:8px;font-size:22px;font-weight:500;color:#444}
.partner i{display:block;width:12px;height:12px;background:var(--green)}

/* footer */
.footer{left:0;top:2983px;width:1200px;height:332px;background:var(--footer)}
.footer-bar{left:0;top:3315px;width:1200px;height:67px;background:var(--footer-bar);text-align:center;color:#999;font-size:13px;line-height:60px}
.foot-brand{left:136px;top:3080px;width:200px;text-align:center;color:var(--green);font-size:34px;font-weight:700;letter-spacing:2px}
.foot-brand small{display:block;font-size:13px;letter-spacing:1px;margin-top:6px}
.foot-col{top:3058px;color:#ddd}
.foot-col h5{font-size:17px;font-weight:700;color:var(--white);margin-bottom:14px}
.foot-col li{list-style:none;font-size:14.5px;line-height:27.6px}
.social{display:flex;gap:6px}
.social span{width:38px;height:38px;border:2px solid #ddd;border-radius:50%}
</style>
</head>
<body>

<div class="abs hero" role="img" aria-label="Photo of a surveillance camera on a mount above a city skyline at dusk"></div>

<div class="abs topbar" style="left:118px;top:32px">
  <svg class="mail-icon" width="18" height="13" viewBox="0 0 18 13"><rect x="0.5" y="0.5" width="17" height="12" fill="#fff"/><path d="M1 1l8 6 8-6" fill="none" stroke="#3a5fc7" stroke-width="1.4"/></svg>contact@tmrdbllc.com
</div>
<div class="abs topbar" style="left:873px;top:30px">
  <svg class="mail-icon" width="16" height="16" viewBox="0 0 24 24" style="margin-right:3px"><path d="M6.6 10.8a15 15 0 0 0 6.6 6.6l2.2-2.2a1 1 0 0 1 1-.25 11.4 11.4 0 0 0 3.6.57 1 1 0 0 1 1 1V20a1 1 0 0 1-1 1A17 17 0 0 1 3 4a1 1 0 0 1 1-1h3.5a1 1 0 0 1 1 1c0 1.25.2 2.45.57 3.57a1 1 0 0 1-.25 1z" fill="#fff"/></svg>+1 (555) 010-4821
</div>

<nav class="nav">
  <a class="active" href="#" style="left:114px">HOME</a>
  <a href="#" style="left:188px">COMPANY OVERVIEW</a>
  <a href="#" style="left:364px">WHO ARE WE</a>
  <a href="#" style="left:752px">OUR PARTNERS AND CLIENTS</a>
  <a href="#" style="left:985px">CONTACT US</a>
</nav>

<div class="abs brand">TMRDB<small>DEFENSE BUREAU, LLC</small></div>

<div class="abs hero-title">
  <h1>SURVEILLANCE CAMERA</h1>
  <h2>INSTALLATIONS &amp; TRAINING</h2>
  <p>Curabitur vel dolor ultrices ipsum dictum tristique<br>Praesent vitae lacus Ut velit enim</p>
  <a class="btn-solid" href="#" style="width:178px;height:47px;line-height:47px;margin-top:24px">LEARN MORE</a>
</div>

<div class="abs dots"><span class="on"></span><span></span><span></span><span></span></div>

<section class="abs intro" style="top:780px">
  <h2>TRIMARK RIDGE DEFENSE</h2>
  <h3>BUREAU, LLC (TMRDB, LLC)</h3>
  <p>We are a Self-certified Small Disabled Veteran Owned Business headquartered in Columbus, Georgia, the Home of the Infantry. We support our clients by supporting security, training and operational needs by using the experience gained through our military service in special operations and advance infantry tactics.</p>
</section>

<div class="abs card" style="left:130px">
  <div class="ico"><svg width="48" height="48" viewBox="0 0 48 48" fill="none" stroke="#fff" stroke-width="2.4"><rect x="6" y="12" width="26" height="11" rx="2" transform="rotate(20 19 17)"/><path d="M22 28l4 8M36 14v22M32 36h8"/></svg></div>
  <h4>OUR MISSION</h4>
  <p>TMRDB, LLC provides premier technology systems intergrades and services in our market, engaging the best talents and strong</p>
  <a class="btn-line" href="#">LEARN MORE</a>
</div>
<div class="abs card" style="left:454px">
  <div class="ico dark"><svg width="46" height="46" viewBox="0 0 48 48" fill="none" stroke="#fff" stroke-width="2.4"><path d="M10 26l8-10h10l10 10-8 8H18z"/><path d="M18 16l6 8 6-8"/></svg></div>
  <h4>OUR VALUES</h4>
  <p>Our core and moral values are what our company operates within trust, loyalty and integrity in the conduct of daily operations</p>
  <a class="btn-line" href="#">LEARN MORE</a>
</div>
<div class="abs card" style="left:776px">
  <div class="ico"><svg width="48" height="48" viewBox="0 0 48 48" fill="none" stroke="#fff" stroke-width="2.4"><path d="M6 14V6h8M34 6h8v8M42 34v8h-8M14 42H6v-8"/><path d="M8 24c5-7 11-10 16-10s11 3 16 10c-5 7-11 10-16 10S13 31 8 24z"/><circle cx="24" cy="24" r="5"/></svg></div>
  <h4>COMPANY OVERVIEW</h4>
  <p>A complete camera technical service company that installs, monitors, repairs, manage and maintain surveillance cameras</p>
  <a class="btn-line" href="#">LEARN MORE</a>
</div>

<div class="abs grey-bg"></div>
<svg class="abs services-band" width="1200" height="700" viewBox="0 0 1200 700" aria-hidden="true">
  <defs><linearGradient id="greenBand" x1="0" y1="0" x2="1" y2="1"><stop offset="0" stop-color="#1a9a0c"/><stop offset=".5" stop-color="#2fb41d"/><stop offset="1" stop-color="#169208"/></linearGradient></defs>
  <polygon points="0,0 560,95 0,150" fill="var(--grey-band)"/>
  <polygon points="0,150 1200,25 1200,492 0,623" fill="url(#greenBand)"/>
</svg>
<div class="abs" role="img" aria-label="Faint background photo of a security camera tinted green" style="left:360px;top:1330px;width:840px;height:480px;background:radial-gradient(ellipse at 60% 40%,rgba(255,255,255,.12),rgba(255,255,255,0) 65%)"></div>

<section class="abs services-head">
  <h2>SERVICES &amp; PRODUCTS</h2>
  <p>Technical Services: Surveillance camera installations, training and maintenance. Logistical Services: Supply management systems to include inventory, accountability, shipping, receiving and warehouse</p>
</section>

<div class="abs tile" style="left:118px" role="img" aria-label="Photo of a security camera mounted on a glass office tower">
  <div style="position:absolute;inset:0;background:linear-gradient(160deg,#c9d8ea 0%,#6f8fb5 50%,#2f4e7a 100%)"></div>
  <div class="label">INSTALLATIONS</div>
</div>
<div class="abs tile training" style="left:448px">
  <div class="inner">
    <h3>TRAINING</h3>
    <p>Praesent elementum elit at tellus Curabitur metus ipsum luctus eu malesuada ut tincidunt sed diam vdisse risus nibh ultricies eu volutpat non condimentu</p>
    <a class="btn-line" href="#">LEARN MORE</a>
  </div>
</div>
<div class="abs tile" style="left:777px" role="img" aria-label="Photo of a technician installing a camera under a roof eave">
  <div style="position:absolute;inset:0;background:linear-gradient(160deg,#8a3a2a 0%,#c9c2b4 35%,#6d8fb8 60%,#2f4f88 100%)"></div>
  <div class="label">MAINTENANCE</div>
</div>

<section class="abs feature">
  <div class="photo" role="img" aria-label="Photo of dome and bullet security cameras on a pole"></div>
  <div class="copy">
    <h3>SURVEILLANCE<br>CAMERAS SYSTEM</h3>
    <p>Etiam eleifend metus vitae adipiscing semper mauris ipsum iaculis elit congue gravida elit mi</p>
    <p>Maecenas aliquet velit vel turpis Mauris neque metus malesuada nec ultricies sit amet porttitor mattis enim In massa libero interdum nec interdum vel blandit sed nulla In ullamcorper est eget tempor cursus neque</p>
    <a class="btn-line" href="#">LEARN MORE</a>
  </div>
</section>

<svg class="abs" style="left:0;top:2550px" width="1200" height="160" viewBox="0 0 1200 160" aria-hidden="true">
  <polygon points="0,10 510,50 1200,80 1200,160 0,160" fill="#fff"/>
  <polygon points="0,10 510,50 0,138" fill="var(--green)"/>
</svg>

<h2 class="abs partners-title">OUR PARTNERS</h2>
<div class="abs partner" style="left:70px">Northgrid<i></i></div>
<div class="abs partner" style="left:286px"><i></i>Venture Office</div>
<div class="abs partner" style="left:503px">AwardHub</div>
<div class="abs partner" style="left:719px"><i></i>Lumenra Optics</div>
<div class="abs partner" style="left:933px">Vantora</div>

<footer>
  <div class="abs footer"></div>
  <div class="abs foot-brand">TMRDB<small>DEFENSE BUREAU, LLC</small></div>
  <div class="abs foot-col" style="left:398px">
    <h5>COMPANY</h5>
    <ul><li>Home</li><li>Company Overview</li><li>Our Partners and CLIENTS</li><li>Who Are We</li><li>Contact</li></ul>
  </div>
  <div class="abs foot-col" style="left:634px">
    <h5>CONTACT US</h5>
    <ul><li>4120 Harbor Pine Road</li><li>Columbus, GA 31999</li><li>+1 (555) 010-4836</li><li>contact@tmrdbllc.com</li><li>www.tmrdbllc.com</li></ul>
  </div>
  <div class="abs foot-col" style="left:882px">
    <h5>FOLLOW US</h5>
    <div class="social">
      <span role="img" aria-label="Social profile link"></span>
      <span role="img" aria-label="Social profile link"></span>
      <span role="img" aria-label="Social profile link"></span>
      <span role="img" aria-label="Social profile link"></span>
    </div>
  </div>
  <div class="abs footer-bar">© 2020 Company Name | All Rights Reserved</div>
</footer>

</body>
</html>
```